Keystone Tap Group Requires Head Turning Truck Wrap Design

We need a head turning, eye catching, standout wrap design for our company vehicles. Our original got the job done but it's time to upgrade. It needs to be sleek, modern and emphasize professionalism. We are a premium brand built on exceptional service and lasting client relationships. Please done include any design on the black cap at the rear of the truck, it should only be on the actual truck itself.

Target Market(s)

Everyone

Industry/Entity Type

Plumbing

Colors
0054AA
0677BA
7BADD7
CADEEF
E8F1F8

Requirements
Should not have
• Cartoon Characters, Cartoon Looking Design, Any Design on the Truck Bed Cap.

```html
<!DOCTYPE html>
<html lang="en">
<head>
<meta charset="utf-8">
<title>Keystone Tap Group – Vehicle Wrap Layout</title>
<link href="https://fonts.googleapis.com/css2?family=Michroma&family=Oswald:wght@500&family=Roboto+Condensed:wght@700&display=swap" rel="stylesheet">
<style>
  :root{
    --wrap-black:#111214;
    --wrap-blue:#2b93d1;
    --ink-dark:#0d1a2a;
    --ink-light:#ffffff;
    --badge-line:#cadeef;
    --canvas:#ffffff;
  }
  html,body{margin:0;padding:0;overflow:hidden;background:var(--canvas);}
  .canvas{width:1200px;height:1200px;position:relative;background:var(--canvas);}
  .wrap-art{position:absolute;left:0;top:0;width:1200px;height:1200px;}
  .panel-black{fill:var(--wrap-black);}
  .panel-blue{fill:var(--wrap-blue);}
  .brand-square{fill:var(--wrap-blue);}
  .brand-name{font-family:"Michroma",sans-serif;fill:var(--wrap-blue);}
  .tagline{font-family:"Oswald",sans-serif;font-weight:500;fill:var(--ink-dark);}
  .tagline-accent{fill:var(--ink-light);}
  .phone{font-family:"Michroma",sans-serif;fill:var(--ink-dark);}
  .web{font-family:"Roboto Condensed",sans-serif;font-weight:700;fill:var(--badge-line);}
  .web-light{fill:var(--ink-light);}
  .licence{font-family:"Michroma",sans-serif;fill:var(--ink-light);}
  .badge-ring{fill:none;stroke:var(--badge-line);stroke-width:2.5;}
  .badge-text{font-family:"Michroma",sans-serif;fill:var(--badge-line);}
</style>
</head>
<body>
<main class="canvas">
<svg class="wrap-art" viewBox="0 0 1200 1200" xmlns="http://www.w3.org/2000/svg">

  <g class="side-view">
    <rect class="panel-black" x="55" y="230" width="1095" height="175" rx="6"/>
    <polygon class="panel-blue" points="55,230 392,230 432,404 55,404"/>
    <polygon class="panel-black" points="55,360 120,360 150,404 55,404"/>
    <polygon class="panel-blue" points="432,345 880,372 880,404 432,404"/>
    <polygon class="panel-blue" points="1000,262 1150,278 1150,302 1000,290"/>
    <polygon class="panel-blue" points="880,372 1150,395 1150,404 880,404"/>

    <text class="tagline" x="80" y="256" font-size="17">PROFESSIONAL SERVICE <tspan class="tagline-accent">IS OUR STANDARD</tspan></text>
    <text class="phone" x="125" y="283" font-size="22">555-014-2276</text>

    <g class="badge-24-7">
      <circle class="badge-ring" cx="137" cy="321" r="30"/>
      <text class="badge-text" x="116" y="316" font-size="13">24</text>
      <line x1="124" y1="340" x2="148" y2="302" stroke="var(--badge-line)" stroke-width="2.5"/>
      <text class="badge-text" x="144" y="337" font-size="13">7</text>
    </g>

    <g class="brand-lockup">
      <rect class="brand-square" x="452" y="290" width="34" height="34"/>
      <text class="brand-name" x="500" y="320" font-size="28" textLength="470" lengthAdjust="spacingAndGlyphs">KEYSTONE TAP GROUP</text>
    </g>
    <text class="web" x="445" y="388" font-size="20">www.ktg.works</text>
  </g>

  <g class="rear-view">
    <rect class="panel-black" x="398" y="727" width="400" height="165" rx="4"/>
    <polygon class="panel-blue" points="398,727 550,727 550,755 580,760 620,760 650,755 650,727 798,727 798,768 398,768"/>
    <text class="licence" x="405" y="741" font-size="7.5">PH51730</text>
    <text class="licence" x="405" y="752" font-size="7.5">RGSA 0000417265081</text>
    <text class="phone" x="795" y="742" font-size="12" text-anchor="end">555-014-2276</text>
    <text class="web web-light" x="795" y="758" font-size="13" text-anchor="end">www.ktg.works</text>
    <rect class="panel-black" x="398" y="760" width="400" height="8"/>
    <g class="brand-lockup">
      <rect class="brand-square" x="414" y="804" width="32" height="32"/>
      <text class="brand-name" x="460" y="830" font-size="22" textLength="322" lengthAdjust="spacingAndGlyphs">KEYSTONE TAP GROUP</text>
    </g>
  </g>
</svg>
</main>
</body>
</html>
```